Electrical Contracting business website design

Website needed to help promote an online footprint focused on local customers in my area Gympie, QLD,Australia 4570

I am after a clear website (one where my customer does not get lost or frustrated)
most important is to engage customer to Call now or Request a quote with all the lead details.

Some bread and butter work for us is broken hot water units, electrical faults and renovators

We offer all sorts of services
- smoke alarms
- Test n Tag
- Lighting
- Fans
- A/C
- Design and planning
- safety switches
- underground Power
- Energy efficient solutions
- hot water repair
- Fault finding
- Control / Automation

Target Market(s)

Local Customers, Renovators, Builders, Commercial, Industrial, Domestic

Industry/Entity Type

Electrician

Coding

Coded - Design and coding required

Number of Pages Required

1 page

Colors
f78f20
000000
ec1f27
ffffff

Requirements
Must have
• Easy to use website with clear Contact Information (call now button)
• Ph: 0452916037 24/7
• Email Brightlinepower@mailnest.example
• , Quote request to receive leads and customer info

```html
<!DOCTYPE html>
<html lang="en">
<head>
<meta charset="utf-8">
<title>Brightline Power – Electrical Contracting</title>
<link rel="stylesheet" href="https://fonts.googleapis.com/css2?family=Montserrat:wght@400;500;600;700&family=Open+Sans:ital,wght@0,400;0,600;0,700;1,400;1,600&display=swap">
<style>
:root{
  --orange:#f78f20;
  --red:#ec1f27;
  --black:#000000;
  --white:#ffffff;
  --ink:#1c1c1c;
  --text:#777777;
  --soft:#efefef;
  --footer:#1f1f24;
  --grad:linear-gradient(90deg,var(--red),var(--orange));
}
*{box-sizing:border-box;margin:0;padding:0}
html,body{width:1200px;height:4197px;overflow:hidden}
body{position:relative;background:var(--white);font-family:'Open Sans',sans-serif;color:var(--ink)}
.abs{position:absolute}
.btn{position:absolute;display:flex;align-items:center;justify-content:center;background:var(--grad);color:var(--white);border-radius:30px;font-family:'Open Sans',sans-serif;font-weight:600;box-shadow:0 4px 10px rgba(236,31,39,.25)}

/* header */
.brand{left:90px;top:18px;display:flex;align-items:center;gap:12px}
.brand-mark{width:42px;height:42px;border-radius:50%;background:var(--orange)}
.brand-name{font-family:'Montserrat',sans-serif;font-weight:700;font-size:27px;color:var(--red);letter-spacing:1px}
.contact-top{display:flex;align-items:center;gap:16px}
.icon-circle{width:50px;height:50px;border-radius:50%;background:var(--grad);display:flex;align-items:center;justify-content:center}
.contact-top small{display:block;font-size:13px;color:var(--ink)}
.contact-top strong{display:block;font-weight:600;color:var(--ink)}
.nav{left:0;top:104px;width:1200px;height:46px;background:linear-gradient(90deg,var(--red),var(--orange) 50%,var(--red))}
.nav a{position:absolute;top:12px;transform:translateX(-50%);color:var(--white);text-decoration:none;font-family:'Montserrat',sans-serif;font-weight:500;font-size:17px}
.nav a.active{font-weight:700}

/* hero */
.hero{left:0;top:150px;width:1200px;height:650px;clip-path:polygon(0 0,100% 0,100% 86%,0 100%);background:linear-gradient(160deg,#5a5f66 0%,#3a3b3e 35%,#8a6a45 55%,#2b2a29 75%,#1a1a1a 100%)}
.hero-title{left:90px;top:90px;font-weight:700;font-size:68px;line-height:62px;color:var(--white)}
.hero-sub{left:93px;top:222px;font-style:italic;font-size:21px;color:var(--white)}
.quote{left:737px;top:75px;width:373px;height:420px;background:rgba(40,40,40,.72);border-radius:4px}
.quote h2{position:absolute;top:30px;width:100%;text-align:center;font-weight:400;font-size:32px;color:var(--white)}
.field{position:absolute;left:24px;width:326px;height:43px;background:var(--white);border-radius:3px;padding:12px 14px;font-size:16px;color:#888}
.dots{left:547px;top:497px;display:flex;gap:14px}
.dots span{width:16px;height:16px;border-radius:50%;border:2px solid var(--white)}
.dots span.on{background:var(--red)}

/* welcome */
.pill{position:absolute;left:0;height:49px;border-radius:25px;background:#e9e9e9}
.welcome-small{left:517px;top:965px;font-family:'Montserrat',sans-serif;font-size:28px}
.welcome-big{left:517px;top:995px;font-family:'Montserrat',sans-serif;font-weight:700;font-size:45px;color:var(--orange)}
.para{position:absolute;left:517px;width:594px;font-size:16px;line-height:35px;color:var(--text);text-align:justify}

/* sections */
.sec-title{position:absolute;left:0;width:1200px;text-align:center;font-family:'Montserrat',sans-serif;font-weight:700;font-size:41px;line-height:50px;color:var(--ink)}
.sec-title em{font-style:normal;color:var(--orange)}
.work{position:absolute;top:1686px;width:325px}
.work-img{height:216px;box-shadow:0 0 0 3px #fff,0 2px 8px rgba(0,0,0,.25)}
.work h3{margin-top:24px;max-width:300px;font-family:'Montserrat',sans-serif;font-weight:500;font-size:23px;line-height:30px;text-transform:uppercase}
.work p{margin-top:10px;font-size:17px;line-height:27px;color:var(--text)}
.services{left:0;top:2232px;width:1200px;height:793px;background:var(--soft)}
.tile{position:absolute;width:229px;height:217px;background:var(--white);display:flex;flex-direction:column;align-items:center;justify-content:flex-start;padding-top:52px}
.tile svg{width:62px;height:62px}
.tile span{margin-top:26px;font-family:'Montserrat',sans-serif;font-weight:500;font-size:23px}

/* testimonials */
.tcard{position:absolute;top:3236px;width:324px;height:248px;background:var(--white);box-shadow:0 2px 14px rgba(0,0,0,.2);text-align:center}
.tcard h4{margin-top:80px;font-weight:600;font-size:16px}
.tcard p{margin:16px 22px 0;font-style:italic;font-size:12.5px;line-height:24px;color:#888}
.avatar{position:absolute;top:3180px;width:112px;height:112px;border-radius:50%;border:5px solid var(--red);box-shadow:0 0 0 3px var(--orange);background:linear-gradient(160deg,#d9c3b0,#8a6b58)}
.arrow{position:absolute;top:3340px;width:46px;height:46px;background:var(--white);box-shadow:0 2px 8px rgba(0,0,0,.15);display:flex;align-items:center;justify-content:center}

/* footer */
.footer-bg{left:0;top:3640px;width:1200px;height:557px}
.fcontact{display:flex;align-items:center;gap:14px;color:var(--white);font-size:14px;line-height:22px}
.fcontact .icon-circle{width:44px;height:44px}
.fhead{font-size:22px;color:var(--white)}
.flinks{list-style:none;font-size:12.5px;line-height:22.5px;color:var(--white)}
.newsletter{left:673px;top:3950px;width:302px;height:43px;display:flex}
.newsletter div:first-child{flex:1;background:var(--white);font-size:13px;color:#555;padding:13px 16px}
.newsletter div:last-child{width:48px;background:var(--grad);display:flex;align-items:center;justify-content:center}
.copy{font-size:11.5px;color:var(--white)}
.social{width:14px;height:14px;border-radius:50%;background:var(--white)}
</style>
</head>
<body>

<!-- header -->
<div class="abs brand"><span class="brand-mark"></span><span class="brand-name">BRIGHTLINE POWER</span></div>
<div class="abs contact-top" style="left:515px;top:24px">
  <div class="icon-circle"><svg width="22" height="16" viewBox="0 0 22 16"><rect x="1" y="1" width="20" height="14" rx="2" fill="none" stroke="#fff" stroke-width="2"/><path d="M1 2l10 7 10-7" fill="none" stroke="#fff" stroke-width="2"/></svg></div>
  <div><small>Email :</small><strong style="font-size:17px">Brightlinepower@mailnest.example</strong></div>
</div>
<div class="abs contact-top" style="left:890px;top:24px">
  <div class="icon-circle"><svg width="22" height="16" viewBox="0 0 22 16"><rect x="1" y="1" width="20" height="14" rx="2" fill="none" stroke="#fff" stroke-width="2"/><path d="M1 2l10 7 10-7" fill="none" stroke="#fff" stroke-width="2"/></svg></div>
  <div><small>Call :</small><strong style="font-size:26px">0452916037</strong></div>
</div>

<nav class="abs nav">
  <a class="active" style="left:215px">HOME</a>
  <a style="left:334px">ABOUT</a>
  <a style="left:483px">WHAT WE DO</a>
  <a style="left:641px">SERVICES</a>
  <a style="left:805px">TESTIMONIALS</a>
  <a style="left:970px">CONTACT</a>
</nav>

<!-- hero -->
<section class="abs hero" role="img" aria-label="Electrician with a work truck under power lines at sunset">
  <svg class="abs" style="left:0;top:0" width="300" height="650" viewBox="0 0 300 650"><defs><linearGradient id="swoosh" x1="0" y1="0" x2="0" y2="1"><stop offset="0" stop-color="#f78f20"/><stop offset="1" stop-color="#ec1f27"/></linearGradient></defs><path d="M0 60 C30 260 70 470 120 620 C130 645 150 650 170 650 L0 650Z" fill="url(#swoosh)"/></svg>
  <div class="abs hero-title">Brightline<br>Power</div>
  <div class="abs hero-sub">Lorem ipsum dolor sit amet, consectetur adipiscing eli.</div>
  <div class="btn" style="left:94px;top:305px;width:178px;height:48px;font-size:17px">Read More</div>
  <form class="abs quote">
    <h2>Request a Quote</h2>
    <div class="field" style="top:105px">Name</div>
    <div class="field" style="top:159px">Email</div>
    <div class="field" style="top:212px">Phone No</div>
    <div class="field" style="top:267px;height:97px">Message</div>
    <div class="btn" style="left:108px;top:398px;width:158px;height:47px;font-size:17px">Submit</div>
  </form>
  <div class="abs dots" style="top:497px;left:547px"><span class="on"></span><span></span><span></span><span></span></div>
</section>

<!-- welcome -->
<div class="pill" style="top:994px;width:356px"></div>
<div class="pill" style="top:1083px;width:428px"></div>
<div class="pill" style="top:1165px;width:450px"></div>
<div class="pill" style="top:1252px;width:466px"></div>
<div class="pill" style="top:1338px;width:385px"></div>
<svg class="abs" style="left:0;top:893px" width="430" height="632" viewBox="0 0 430 632" role="img" aria-label="Branded service van parked among tall trees under a cloudy sky">
  <defs><linearGradient id="diamondFill" x1="0" y1="0" x2="0" y2="1"><stop offset="0" stop-color="#4f8fd6"/><stop offset=".4" stop-color="#c9d8e6"/><stop offset=".6" stop-color="#3f5a32"/><stop offset="1" stop-color="#2a3324"/></linearGradient></defs>
  <path d="M70 24 Q95 0 120 24 L400 290 Q425 316 400 342 L120 608 Q95 632 70 608 L-210 342 Q-235 316 -210 290Z" fill="url(#diamondFill)"/>
</svg>
<div class="abs welcome-small">Welcome To</div>
<div class="abs welcome-big">BRIGHTLINE POWER</div>
<p class="para" style="top:1070px">Lorem ipsum dolor sit amet, consectetur adipiscing elit, sed do eiusmod tempor incididunt ut labore et dolore magna aliqua. Ut enim ad minim veniam.</p>
<p class="para" style="top:1152px">Lorem ipsum dolor sit amet, consectetur adipiscing elit, sed do eiusmod tempor incididunt ut labore et dolore magna aliqua. Ut enim ad minim veniam, quis nostrud exercitation ullamco laboris nisi ut aliquip ex ea commodoquat. Duis aute irure dolor in reprehenderit in voluptate velit esse cillum dolore eu fugiat nulla pariatur. Excepteur sint occaecat cupidatat non proident, sunt in culpa qui officia deserunt mollit anim id est laborum</p>
<div class="btn" style="left:518px;top:1397px;width:151px;height:49px;font-size:16px">Read More</div>

<!-- what we do -->
<h2 class="sec-title" style="top:1608px">WHAT WE <em>DO</em></h2>
<article class="work" style="left:90px">
  <div class="work-img" role="img" aria-label="Hands repairing a white hot water unit" style="background:linear-gradient(135deg,#f2f2f2,#cfd3d6 60%,#9aa0a5)"></div>
  <h3>Broken hot water units</h3>
  <p>Lorem ipsum dolor sit amet, adipiscing elit, sed do eiusmod tempor incididunt ut labore et dolore magna</p>
</article>
<div class="btn" style="left:90px;top:2096px;width:131px;height:38px;font-size:14px">Read More</div>
<article class="work" style="left:438px">
  <div class="work-img" role="img" aria-label="Hand testing colourful wiring with a screwdriver" style="background:linear-gradient(135deg,#3a2a1a,#c7781c 50%,#2d2520)"></div>
  <h3>Electrical faults</h3>
  <p>Lorem ipsum dolor sit amet, adipiscing elit, sed do eiusmod tempor incididunt ut labore et dolore magna</p>
</article>
<div class="btn" style="left:438px;top:2096px;width:131px;height:38px;font-size:14px">Read More</div>
<article class="work" style="left:786px">
  <div class="work-img" role="img" aria-label="Renovator sealing a window frame" style="background:linear-gradient(135deg,#d6d8d2,#8d9088 55%,#e6e6e4)"></div>
  <h3>Renovators</h3>
  <p>Lorem ipsum dolor sit amet, adipiscing elit, sed do eiusmod tempor incididunt ut labore et dolore magna</p>
</article>
<div class="btn" style="left:786px;top:2096px;width:131px;height:38px;font-size:14px">Read More</div>

<!-- services -->
<section class="abs services"></section>
<h2 class="sec-title" style="top:2318px">OUR <em>SERVICES</em></h2>
<div class="tile" style="left:115px;top:2400px"><svg viewBox="0 0 62 62" fill="none" stroke="#f78f20" stroke-width="2.5"><ellipse cx="31" cy="26" rx="26" ry="10"/><path d="M5 26v6c0 6 12 11 26 11s26-5 26-11v-6"/><ellipse cx="31" cy="26" rx="12" ry="4"/></svg><span>Smoke Alarms</span></div>
<div class="tile" style="left:362px;top:2400px"><svg viewBox="0 0 62 62" fill="none" stroke="#f78f20" stroke-width="2.5"><path d="M40 10l12 12-22 22-12-12z"/><path d="M18 32l-8 8 12 12 8-8"/><path d="M10 52l-4 6"/><path d="M46 4c4 2 8 6 10 10M50 0c6 3 10 7 12 12"/></svg><span>Test n Tag</span></div>
<div class="tile" style="left:608px;top:2400px"><svg viewBox="0 0 62 62" fill="none" stroke="#f78f20" stroke-width="2.5"><path d="M14 58V16c0-8 6-12 14-12s12 6 12 12"/><path d="M32 20c0 6 16 6 16 0z"/><path d="M6 58h18"/><path d="M40 30l-3 5M46 32v6M52 30l3 5M54 22h6"/></svg><span>Lighting</span></div>
<div class="tile" style="left:855px;top:2400px"><svg viewBox="0 0 62 62" fill="none" stroke="#f78f20" stroke-width="2.5"><circle cx="31" cy="22" r="4"/><path d="M31 18L24 2l14 2zM35 22l16-6-2 14zM27 22l-16-6 2 14zM31 26l-8 12h16z"/><path d="M31 38v16M26 58h10"/></svg><span>Fans</span></div>
<div class="tile" style="left:115px;top:2634px"><svg viewBox="0 0 62 62" fill="none" stroke="#f78f20" stroke-width="2.5"><rect x="4" y="14" width="54" height="40"/><rect x="10" y="20" width="16" height="14"/><rect x="30" y="20" width="22" height="28"/><path d="M10 40h14M10 46h14M36 26h10M36 34h10"/></svg><span>Design &amp; planning</span></div>
<div class="tile" style="left:362px;top:2634px"><svg viewBox="0 0 62 62" fill="none" stroke="#f78f20" stroke-width="2.5"><circle cx="31" cy="8" r="4"/><path d="M31 12v22"/><rect x="20" y="34" width="22" height="8"/><path d="M4 50h54M10 42h42v8"/><path d="M8 58h46"/></svg><span>Safety Switches</span></div>
<div class="tile" style="left:608px;top:2634px"><svg viewBox="0 0 62 62" fill="none" stroke="#f78f20" stroke-width="2.5"><circle cx="31" cy="31" r="26"/><rect x="12" y="20" width="22" height="22"/><circle cx="42" cy="31" r="8"/><path d="M16 26h4M24 26h4M16 32h14M16 38h14M42 23v16"/></svg><span>Fault finding</span></div>
<div class="tile" style="left:855px;top:2634px"><svg viewBox="0 0 62 62" fill="none" stroke="#f78f20" stroke-width="2.5"><path d="M14 12c0-8 34-8 34 0v34c0 8-34 8-34 0z"/><path d="M14 12c0 6 34 6 34 0"/><path d="M26 52v8M36 52v8M30 26v12M27 34h6"/></svg><span>Hot water repair</span></div>
<div class="btn" style="left:535px;top:2886px;width:130px;height:41px;font-size:14px">View All</div>

<!-- testimonials -->
<h2 class="sec-title" style="top:3110px">TESTIMONIALS</h2>
<div class="tcard" style="left:90px"><h4>Mia Carter</h4><p>"Lorem ipsum dolor sit amet, consectetur adipiscing elit, sed do eiusmod tempor incididunt ut labore et dolore magna aliqua. Ut enim ad minim veniam, quis nostrud exercitation"</p></div>
<div class="tcard" style="left:438px"><h4>Liam Brooks</h4><p>"Lorem ipsum dolor sit amet, consectetur adipiscing elit, sed do eiusmod tempor incididunt ut labore et dolore magna aliqua. Ut enim ad minim veniam, quis nostrud exercitation"</p></div>
<div class="tcard" style="left:786px"><h4>Noah Ellis</h4><p>"Lorem ipsum dolor sit amet, consectetur adipiscing elit, sed do eiusmod tempor incididunt ut labore et dolore magna aliqua. Ut enim ad minim veniam, quis nostrud exercitation"</p></div>
<div class="avatar" style="left:196px" role="img" aria-label="Portrait of customer Mia Carter"></div>
<div class="avatar" style="left:544px" role="img" aria-label="Portrait of customer Liam Brooks"></div>
<div class="avatar" style="left:892px" role="img" aria-label="Portrait of customer Noah Ellis"></div>
<div class="arrow" style="left:22px"><svg width="18" height="10" viewBox="0 0 18 10"><path d="M18 5H3M6 1L2 5l4 4" fill="none" stroke="#222" stroke-width="2"/></svg></div>
<div class="arrow" style="left:1132px"><svg width="18" height="10" viewBox="0 0 18 10"><path d="M0 5h15M12 1l4 4-4 4" fill="none" stroke="#222" stroke-width="2"/></svg></div>
<div class="btn" style="left:537px;top:3518px;width:124px;height:39px;font-size:14px">VIEW ALL</div>

<!-- footer -->
<svg class="abs footer-bg" viewBox="0 0 1200 557" width="1200" height="557">
  <defs><linearGradient id="footSwoosh" x1="0" y1="0" x2="0" y2="1"><stop offset="0" stop-color="#f78f20"/><stop offset="1" stop-color="#ec1f27"/></linearGradient></defs>
  <path d="M0 95 L980 20 C1010 16 1025 25 1035 45 L1200 400 L1200 557 L0 557Z" fill="#1f1f24"/>
  <path d="M1060 65 C1100 45 1130 55 1150 90 C1170 130 1185 170 1200 210 L1200 520 C1160 400 1110 220 1060 65Z" fill="url(#footSwoosh)"/>
</svg>
<div class="abs fcontact" style="left:90px;top:3760px">
  <div class="icon-circle"><svg width="16" height="22" viewBox="0 0 16 22"><path d="M8 0C3.6 0 0 3.4 0 7.8 0 13 8 22 8 22s8-9 8-14.2C16 3.4 12.4 0 8 0z" fill="#fff"/><circle cx="8" cy="8" r="3" fill="#ec1f27"/></svg></div>
  <div>27 Harbour Lane, Suite 4<br>Riverton, QLD 4570</div>
</div>
<div class="abs fcontact" style="left:368px;top:3760px">
  <div class="icon-circle"><svg width="18" height="13" viewBox="0 0 22 16"><rect x="1" y="1" width="20" height="14" rx="2" fill="#fff"/><path d="M1 2l10 7 10-7" fill="none" stroke="#ec1f27" stroke-width="2"/></svg></div>
  <div>Email<br>Brightlinepower@mailnest.example</div>
</div>
<div class="abs fcontact" style="left:662px;top:3760px">
  <div class="icon-circle"><svg width="18" height="18" viewBox="0 0 24 24"><path d="M6.6 10.8c1.4 2.8 3.8 5.1 6.6 6.6l2.2-2.2c.3-.3.7-.4 1-.2 1.1.4 2.3.6 3.6.6.6 0 1 .4 1 1V20c0 .6-.4 1-1 1C10.6 21 3 13.4 3 4c0-.6.4-1 1-1h3.5c.6 0 1 .4 1 1 0 1.3.2 2.5.6 3.6.1.3 0 .7-.2 1z" fill="#fff"/></svg></div>
  <div>0452916037</div>
</div>

<div class="abs fhead" style="left:89px;top:3895px">Other Links</div>
<ul class="abs flinks" style="left:90px;top:3946px"><li>Home</li><li>About</li><li>What We Do</li><li>Services</li><li>Testimonials</li><li>Contact</li></ul>
<div class="abs fhead" style="left:380px;top:3895px">Legal</div>
<ul class="abs flinks" style="left:381px;top:3946px"><li>Faq</li><li>Privacy Policy</li><li>Sitemap</li></ul>
<div class="abs fhead" style="left:671px;top:3895px">Newsletter</div>
<div class="abs newsletter"><div>Email Address</div><div><svg width="20" height="18" viewBox="0 0 20 18"><path d="M0 8L20 0 16 18 10 12 16 4 8 10z" fill="#fff"/></svg></div></div>

<div class="abs copy" style="left:90px;top:4108px">© Copyrights.2019.The Company Name.All Rights Reserved</div>
<div class="abs copy" style="left:889px;top:4108px;display:flex;align-items:center;gap:10px">Connect With Us : <span class="social"></span><span class="social"></span></div>

</body>
</html>
```